Forget what you know about corporate well

I need a one-page flies used for print, to embedding in a website, all social media platforms and email.

Target Market(s)

Business

Industry/Entity Type

Health And Wellness

Font styles to use
Serif
Script
Other font styles liked:
• I would like the designers opinion on the font

Colors

Designer to choose colors to be used in the design.

Requirements
Must have
• This is the wording:
• Did you know that 75% of healthcare costs are incurred by preventable diseases? Cardiovascular disease, cancer, and diabetes are the three major causes of rising health care plans and are all preventable.
• Owen and his team have spent decades learning how to increase productivity, reduce absenteeism, and increase employee engagement, all leading to lowering healthcare costs. Together, they have developed a system created to target the masses all while addressing individual needs. Their corporate training challenges helps to engrain positive habits through a carefully curated accountability and reward system.
• How it works:
• Step 1 – evaluate the needs of your business;
• Step 2 – set up individualized workshops based on highest needs;
• Step 3 – create a customized corporate training challenge.
• Why Owen?
• Owen excels at motivational speaking. He is an author, a nutritionist and a professional athlete with a master’s degree in clinical nutrition. He is a teacher of corporate wellness at Marbrook College and a health coach. Owen has been featured in national magazines, podcasts, and popular fitness websites. Owen’s own health issues put him on a quest to heal himself and others. With twenty-five years of experience and a passion for wellness, he can provide your company with an unforgettable experience.
Nice to have
• I will not give my opinion, I believe that is an insult to the designer. All of the verbiage is above and I attached a plethora of pictures.
Should not have
• No opinion

```html
<!DOCTYPE html>
<html lang="en">
<head>
<meta charset="utf-8">
<title>Vital Shift Wellness – Corporate Flyer</title>
<link rel="stylesheet" href="https://fonts.googleapis.com/css2?family=Montserrat:wght@400;600;700;800&family=Open+Sans:wght@400;600&family=Great+Vibes&display=swap">
<style>
  :root {
    --lime: #9cc31b;
    --lime-light: #c4dc5e;
    --lime-pale: #e3efb4;
    --charcoal: #3c3d3f;
    --charcoal-deep: #2e2f31;
    --ink: #333;
    --paper: #ffffff;
    --mist: #eceded;
  }
  * { margin: 0; padding: 0; box-sizing: border-box; }
  html, body { width: 804px; height: 1200px; overflow: hidden; background: var(--paper); }
  .flyer { position: relative; width: 804px; height: 1200px; overflow: hidden; font-family: "Open Sans", sans-serif; color: var(--ink); background: linear-gradient(180deg, #fafafa 0%, var(--mist) 100%); }
  .backdrop { position: absolute; inset: 0; }
  .fact-box { position: absolute; top: 24px; right: 0; width: 264px; padding: 30px 24px 0 20px; color: #fff; font-family: "Montserrat", sans-serif; font-size: 17px; line-height: 1.4; font-weight: 600; text-align: right; }
  .fact-box em { font-style: normal; color: var(--lime); font-weight: 700; }
  .brand { position: absolute; left: 60px; top: 178px; width: 360px; text-align: center; }
  .brand-mark { display: inline-block; width: 62px; height: 62px; border-radius: 50%; border: 5px solid var(--lime); }
  .brand-name { margin-top: 14px; font-family: "Montserrat", sans-serif; font-weight: 700; font-size: 33px; color: var(--lime); letter-spacing: -0.3px; }
  .photo { position: absolute; }
  .photo-speaker { left: 26px; top: 312px; width: 330px; height: 250px; background: linear-gradient(135deg, #6c6a66, #3d3c3a 60%, #8e8478); }
  .photo-audience { left: 40px; top: 565px; width: 300px; height: 120px; background: linear-gradient(120deg, #4a4744, #7a7068); clip-path: polygon(0 0, 100% 0, 78% 100%, 0 100%); }
  .photo-athlete { left: 430px; top: 210px; width: 340px; height: 350px; background: linear-gradient(160deg, #e6e2df 0%, #cfbfb3 45%, #b99a8a 70%, #d9d3cf 100%); }
  .profile { position: absolute; left: 452px; top: 572px; width: 330px; color: #e8e8e8; }
  .profile-name { font-family: "Great Vibes", cursive; font-size: 40px; color: #fff; margin-bottom: 8px; text-align: center; }
  .profile p { font-size: 11px; line-height: 1.45; text-align: center; margin-bottom: 8px; }
  .section-tag { position: absolute; left: 28px; height: 36px; padding: 0 26px 0 14px; display: flex; align-items: center; background: var(--lime); color: #fff; font-family: "Montserrat", sans-serif; font-weight: 800; font-size: 18px; clip-path: polygon(0 0, 100% 0, 90% 100%, 0 100%); }
  .tag-how { top: 842px; }
  .tag-why { top: 1010px; }
  .steps { position: absolute; left: 34px; top: 890px; list-style: none; }
  .steps li { display: flex; align-items: center; gap: 12px; font-size: 17px; margin-bottom: 12px; color: var(--ink); }
  .step-tick { width: 24px; height: 24px; flex: none; }
  .why-copy { position: absolute; left: 30px; top: 1058px; width: 744px; font-size: 14px; line-height: 1.5; color: var(--ink); }
  .footer-bar { position: absolute; left: 0; bottom: 0; width: 804px; height: 34px; background: var(--lime); }
  .footer-url { position: absolute; right: 30px; bottom: 8px; font-family: "Montserrat", sans-serif; font-size: 15px; font-weight: 600; color: #fff; letter-spacing: 1.5px; }
</style>
</head>
<body>
<main class="flyer">
  <svg class="backdrop" width="804" height="1200" viewBox="0 0 804 1200" aria-hidden="true">
    <polygon points="540,24 804,24 804,200 560,200" fill="var(--charcoal)"/>
    <polygon points="0,700 804,130 804,200 0,770" fill="var(--lime-pale)" opacity="0.6"/>
    <polygon points="300,800 804,420 804,470 330,820" fill="var(--lime)"/>
    <polygon points="260,760 804,360 804,390 280,780" fill="var(--lime-light)"/>
    <polygon points="330,840 804,470 804,520 380,840" fill="var(--lime)"/>
    <polygon points="560,1000 804,860 804,905 650,1000" fill="var(--lime)"/>
    <polygon points="520,1000 804,880 804,895 550,1000" fill="var(--lime-light)"/>
    <polygon points="680,1000 804,915 804,1000" fill="var(--charcoal-deep)"/>
  </svg>

  <div class="photo photo-athlete" role="img" aria-label="Photo of a woman in a standing yoga pose, holding one leg high above her head"></div>

  <svg class="backdrop" width="804" height="1200" viewBox="0 0 804 1200" aria-hidden="true">
    <polygon points="450,560 804,560 804,840 370,840" fill="var(--charcoal)"/>
  </svg>

  <div class="fact-box">Did you know that 75% of <em>healthcare costs are incurred</em> by preventable diseases ?</div>

  <div class="brand">
    <span class="brand-mark" aria-hidden="true"></span>
    <div class="brand-name">Vital Shift Wellness</div>
  </div>

  <div class="photo photo-speaker" role="img" aria-label="Photo of a speaker presenting to a corporate audience"></div>
  <div class="photo photo-audience" role="img" aria-label="Photo of workshop attendees seated at tables"></div>

  <section class="profile">
    <div class="profile-name">Owen T. Marlow</div>
    <p>Cardiovascular disease, cancer, and diabetes are the three major causes of rising health care plans and are all preventable.</p>
    <p>Owen and his team have spent decades learning how to increase productivity, reduce absenteeism, and increase employee engagement, all leading to lowering healthcare costs. Together, they have developed a system created to target the masses all while addressing individual needs. Their corporate training challenges helps to engrain positive habits through a carefully curated accountability and reward system.</p>
  </section>

  <h2 class="section-tag tag-how">HOW IT WORKS ?</h2>
  <ul class="steps">
    <li><svg class="step-tick" viewBox="0 0 24 24"><rect width="24" height="24" rx="3" fill="var(--lime)"/><path d="M6 12.5l4 4 8-9" stroke="#fff" stroke-width="2.6" fill="none" stroke-linecap="round"/></svg>Evaluate the needs of your business.</li>
    <li><svg class="step-tick" viewBox="0 0 24 24"><rect width="24" height="24" rx="3" fill="var(--lime)"/><path d="M6 12.5l4 4 8-9" stroke="#fff" stroke-width="2.6" fill="none" stroke-linecap="round"/></svg>Set up individualized workshops based on highest needs.</li>
    <li><svg class="step-tick" viewBox="0 0 24 24"><rect width="24" height="24" rx="3" fill="var(--lime)"/><path d="M6 12.5l4 4 8-9" stroke="#fff" stroke-width="2.6" fill="none" stroke-linecap="round"/></svg>Create a customized corporate training challenge.</li>
  </ul>

  <h2 class="section-tag tag-why">WHY OWEN ?</h2>
  <p class="why-copy">Owen excels at motivational speaking. He is an author, a nutritionist and a professional athlete with a master’s degree in clinical nutrition. He is a teacher of corporate wellness at Marbrook College and a health coach. Owen has been featured in national magazines, podcasts, and popular fitness websites. Owen’s own health issues put him on a quest to heal himself and others. With twenty-five years of experience and a passion for wellness, he can provide your company with an unforgettable experience.</p>

  <div class="footer-bar"></div>
  <div class="footer-url">www.owenmarlow.com</div>
</main>
</body>
</html>
```